Preisliste für Kosmetikinstitut
Zielgruppe
Ich benötige für mein Kosmetikinstitut eine Preisliste für die moderne Frau, aber auch Männer. Das Design sollte mein Logo enthalten. Farben des Designkonzepts einbauen.
A4 quer zum Falten, wie ein Heft, 1. Seite Preisliste mit logo, im Innenteil dann Anwendungen
Aufgabenstellung
Minimalistisch, ästhetisch, modern, edel
Kontaktdaten auf der Rückseite
LT Hautatelier
Lena Tessmar
Lindenstieg 17
83671 Ostermoor
EMail: lena@lt-hautatelier.de
Whatsapp: 0176 284 9017

```html
<!DOCTYPE html>
<html lang="de">
<head>
<meta charset="utf-8">
<title>LT Hautatelier – Preisliste</title>
<link href="https://fonts.googleapis.com/css2?family=Cormorant+Garamond:wght@400;500;600;700&family=Crimson+Pro:wght@400;500;600&display=swap" rel="stylesheet">
<style>
  :root{
    --stage:#f3ede6;
    --cream:#fbf9f0;
    --gold:#cfa460;
    --slate:#66736f;
    --ink:#2c2a27;
    --white:#fffdf7;
    --head:"Cormorant Garamond", Georgia, serif;
    --body:"Crimson Pro", Georgia, serif;
  }
  *{box-sizing:border-box;margin:0;padding:0}
  html,body{width:1200px;height:2400px;overflow:hidden;background:var(--stage)}
  body{position:relative;font-family:var(--body);color:var(--ink)}
  .spread{position:absolute;left:40px;width:1120px;height:792px;display:flex;box-shadow:0 18px 40px rgba(90,70,40,.12)}
  .spread--outside{top:240px}
  .spread--inside{top:1160px}
  .panel{position:relative;width:373.33px;height:100%;overflow:hidden}
  .panel--gold{background:var(--gold);color:var(--white)}
  .panel--cream{background:var(--cream)}
  .section-title{font-family:var(--head);font-weight:500;text-transform:uppercase;letter-spacing:.06em;font-size:17px;margin-bottom:8px}
  .panel--gold .section-title{color:var(--white)}
  .panel--cream .section-title{color:var(--gold)}
  .copy{font-size:11.5px;line-height:1.45}
  .price-list{list-style:none;margin-top:12px}
  .price-row{display:flex;align-items:baseline;font-size:12px;font-weight:600;margin-top:4px}
  .price-row .leader{flex:1;border-bottom:1px dotted currentColor;margin:0 6px;transform:translateY(-3px)}
  .price-row .amount{font-family:var(--head);font-size:17px;font-weight:700;width:52px;text-align:right}

  /* outside */
  .treatments-outer{padding:56px 34px 0}
  .treatments-outer .block + .block{margin-top:40px}
  .extras{position:absolute;left:0;top:0;width:100%;height:100%}
  .extras-bg{position:absolute;inset:0}
  .extras-list{position:absolute;left:32px;right:30px;top:70px;color:var(--ink)}
  .extras-list .price-row .amount{color:var(--gold)}
  .contact{position:absolute;left:0;right:0;top:520px;text-align:center;color:var(--white)}
  .contact-name{font-family:var(--head);font-size:24px;font-weight:700;letter-spacing:.02em}
  .contact-line{font-size:14px;line-height:1.35}
  .phone-pill{position:absolute;left:24px;right:24px;top:668px;height:50px;border-radius:25px;background:var(--slate);color:var(--white);display:flex;align-items:center;padding-left:30px;gap:14px;font-family:var(--head);font-weight:700;font-size:25px}
  .cover-brand{position:absolute;top:52px;left:0;right:0;text-align:center;font-family:var(--head);font-size:30px;font-weight:500;color:var(--slate);letter-spacing:.08em;text-transform:uppercase;display:flex;justify-content:center;align-items:center;gap:12px}
  .cover-brand .dot{width:10px;height:10px;border-radius:50%;background:var(--gold)}
  .cover-title{position:absolute;top:118px;left:0;right:0;text-align:center;font-family:var(--head);font-weight:700;font-size:40px;letter-spacing:.05em}
  .cover-title .a{color:var(--slate)}
  .cover-title .b{color:var(--gold)}
  .cover-photo{position:absolute;left:0;right:0;top:210px;bottom:0;background:linear-gradient(160deg,#f6ecdf 0%,#e9cdb4 45%,#d9b293 80%,#cfa07f 100%)}

  /* inside */
  .menu{padding:46px 30px 0 34px}
  .menu-heading{font-family:var(--head);font-weight:700;font-size:22px;letter-spacing:.08em;text-transform:uppercase;color:var(--slate);border-bottom:1px solid var(--slate);padding-bottom:6px;margin-bottom:20px;width:82%}
  .item{position:relative;padding-right:62px;margin-bottom:22px}
  .item-title{font-family:var(--head);font-size:15px;font-weight:500;text-transform:uppercase;color:var(--gold);letter-spacing:.04em;line-height:1.15;margin-bottom:4px}
  .item .copy{font-size:11px}
  .duration{font-size:11px;color:var(--gold);font-weight:600;margin-top:3px}
  .badge{position:absolute;right:0;top:40%;width:48px;height:48px;border-radius:50%;background:var(--gold);color:var(--white);display:flex;align-items:center;justify-content:center;font-family:var(--head);font-weight:700;font-size:16px}
  .badge--slate{background:var(--slate)}
  .device{padding:56px 32px 0}
  .device .menu-heading{color:var(--white);border-color:var(--white);width:70%}
  .device .item-title{color:var(--white)}
  .steps{list-style:none;margin-top:10px;counter-reset:s}
  .steps li{counter-increment:s;font-size:11px;line-height:1.4;padding-left:18px;position:relative;margin-bottom:6px}
  .steps li::before{content:counter(s)".";position:absolute;left:0}
  .device .duration{color:var(--white);margin-top:14px;font-size:12px}
  .device .badge{position:absolute;right:36px;top:auto;bottom:130px;width:60px;height:60px;font-size:19px}
  .footer-band{position:absolute;left:373.33px;right:0;top:716px;height:38px;background:var(--slate);border-radius:19px 0 0 19px;color:var(--white);display:flex;align-items:center;padding-left:30px;font-family:var(--head);font-size:17px;letter-spacing:.03em}
</style>
</head>
<body>

<section class="spread spread--outside">
  <article class="panel panel--gold treatments-outer">
    <div class="block">
      <h2 class="section-title">Mikrodermabrasion</h2>
      <p class="copy">Bei der Mikrodermabrasion handelt es sich um ein mechanisches Hautpeeling, dabei werden mittels feinster Kristalle die Hornzellen der obersten Hautschicht schonend abgetragen und dann mit Hilfe eines Unterdrucks behutsam abgesaugt. Der revitalisierende Prozess erhöht die Durchblutung, fördert die Zellerneuerung und verleiht Ihrer Haut ein zartes frisches Gefühl. Die Haut gewinnt an Spannkraft, feine Fältchen werden gemildert und Poren sichtbar verkleinert. Außerdem hilft es bei oberflächlichen Akne Narben, Pigmentstörungen und Dehnungsstreifen. Wirkstoffe können nun wieder besser von der Haut aufgenommen werden.</p>
      <ul class="price-list">
        <li class="price-row"><span>Gesicht</span><span class="leader"></span><span class="amount">€ 89</span></li>
        <li class="price-row"><span>Gesicht, Hals, Dekolleté</span><span class="leader"></span><span class="amount">€ 110</span></li>
      </ul>
    </div>
    <div class="block">
      <h2 class="section-title">Microneedling</h2>
      <p class="copy">Die Behandlung eignet sich besonders für Menschen, die ihre Hautqualität verbessern und Falten, (Akne)Narben, Pigmentverschiebungen, große Poren und sogar Haarausfall behandeln wollen.</p>
      <p class="copy" style="margin-top:8px">Mit Hilfe feinster Nadeln werden der Haut kontrolliert Mikroverletzungen zugeführt, dies regt die natürliche Wundheilung, sowie Kollagen- und Elastin Bildung an. Microneedling ist also eine natürliche Beauty-Behandlung, die körpereigene Reparaturmechanismen nutzt, um ein strafferes Hautbild zu erhalten. Bereits nach der ersten Behandlung sieht die Haut aufgepolstert, frisch und rosig aus. Kleine Linien und Fältchen werden tiefenbehandelt. Die Haut wirkt straffer und jugendlicher. Ein weiterer Vorteil, durch die Stichkanäle können Wirkstoffe besser von der Haut aufgenommen werden.</p>
      <ul class="price-list">
        <li class="price-row"><span>Gesicht</span><span class="leader"></span><span class="amount">€ 110</span></li>
        <li class="price-row"><span>Gesicht, Hals</span><span class="leader"></span><span class="amount">€ 130</span></li>
        <li class="price-row"><span>Gesicht, Hals, Dekolleté</span><span class="leader"></span><span class="amount">€ 150</span></li>
      </ul>
    </div>
  </article>

  <article class="panel panel--gold">
    <div class="extras">
      <svg class="extras-bg" viewBox="0 0 373 792" preserveAspectRatio="none" aria-hidden="true">
        <path d="M0 0H373V250C300 270 250 250 200 268C150 286 90 300 0 310Z" fill="#fbf9f0"/>
      </svg>
      <div class="extras-list">
        <h2 class="section-title" style="color:var(--gold)">Zusatzleistungen</h2>
        <ul class="price-list">
          <li class="price-row"><span>Augenbrauen zupfen</span><span class="leader"></span><span class="amount">€ 8</span></li>
          <li class="price-row"><span>Augenbrauen färben</span><span class="leader"></span><span class="amount">€ 12</span></li>
          <li class="price-row"><span>Wimpern färben</span><span class="leader"></span><span class="amount">€ 8</span></li>
          <li class="price-row"><span>Enthaarung störender<br>Gesichtsbehaarung<br>mittels Wax</span><span class="leader"></span><span class="amount">€ 10-30</span></li>
        </ul>
      </div>
    </div>
    <div class="contact">
      <p class="contact-name">Lena Tessmar</p>
      <p class="contact-line">Lindenstieg 17</p>
      <p class="contact-line">83671 Ostermoor</p>
    </div>
    <div class="phone-pill">
      <svg width="26" height="26" viewBox="0 0 24 24" aria-hidden="true"><path fill="#fffdf7" d="M6.6 10.8a15.1 15.1 0 0 0 6.6 6.6l2.2-2.2c.3-.3.7-.4 1-.2 1.1.4 2.3.6 3.6.6.6 0 1 .4 1 1V20c0 .6-.4 1-1 1A17 17 0 0 1 3 4c0-.6.4-1 1-1h3.5c.6 0 1 .4 1 1 0 1.3.2 2.5.6 3.6.1.3 0 .7-.2 1z"/></svg>
      <span>0176 284 9017</span>
    </div>
  </article>

  <article class="panel panel--cream">
    <div class="cover-brand"><span class="dot"></span>LT Hautatelier</div>
    <h1 class="cover-title"><span class="a">PREIS</span><span class="b">LISTE</span></h1>
    <div class="cover-photo" role="img" aria-label="Porträtfoto einer Frau mit gepflegter Haut, die Hände sanft an den Wangen"></div>
  </article>
</section>

<section class="spread spread--inside">
  <article class="panel panel--cream menu">
    <h2 class="menu-heading">Gesichtsbehandlungen</h2>
    <div class="item">
      <h3 class="item-title">Express Facial Treatment</h3>
      <p class="copy">Für alle, die wenig Zeit haben und trotzdem ihre Haut auffrischen und revitalisieren wollen. Reinigung, Enzympeeling, Serum, Maske, Abschlusspflege</p>
      <p class="duration">Dauer: 35-45 Min.</p>
      <span class="badge">€ 59</span>
    </div>
    <div class="item">
      <h3 class="item-title">Classic Facial Treatment – Klassische Gesichtsbehandlung</h3>
      <p class="copy">Reinigung, Enzympeeling, Vapozon, Ausreinigung, Augenbrauenkorrektur, Ampulle, Maske, individuelle Abschlusspflege</p>
      <p class="duration">Dauer: 45-60 Min.</p>
      <span class="badge">€ 89</span>
    </div>
    <div class="item">
      <h3 class="item-title">Clear Skin Treatment</h3>
      <p class="copy">Die Haut wirkt ausgeglichener. Unreinheiten wird vorgebeugt, der Teint erhält Balance und kann sich beruhigen. Gleichzeitig wird die Haut durch die Hyaluronsäure vitalisiert und Falten und Fältchen kann entgegengewirkt werden.</p>
      <p class="duration">Dauer: 50-60 Min.</p>
      <span class="badge">€ 89</span>
    </div>
    <div class="item">
      <h3 class="item-title">Vasora Treatment</h3>
      <p class="copy">Hautrötungen und Couperose Erscheinungen werden gelindert, die Gefäßwände werden gestärkt und das Hautbild wirkt ausgeglichener. Mögliche Irritationen gehen zurück. Gleichzeitig sorgt die hochkonzentrierte Hyaluronsäure für Frische, Vitalität und Glätte.</p>
      <p class="duration">Dauer: 50-60 Min.</p>
      <span class="badge">€ 89</span>
    </div>
  </article>

  <article class="panel panel--cream menu" style="padding-top:70px">
    <div class="item">
      <h3 class="item-title">Mildara Soft Treatment<br>(für die empfindliche, gereizte Haut)</h3>
      <p class="copy">Entzündliche Prozesse können gemildert werden, gereizte Haut oder solche, die wenig verträgt, wird beruhigt. Irritationen können zurückgehen, die Haut erhält Balance.</p>
      <p class="duration">Dauer: ca. 50 Min.</p>
      <span class="badge">€ 79</span>
    </div>
    <div class="item">
      <h3 class="item-title">Vitamin Soft Boost</h3>
      <p class="copy">Vitamine sorgen für Power und Frische in und auf der Haut, die Widerstandskraft der Haut wird gestärkt. Die Faltentiefe kann gemildert werden.</p>
      <p class="duration">Dauer: ca. 50 Min.</p>
      <span class="badge">€ 79</span>
    </div>
    <div class="item">
      <h3 class="item-title">Anti-Age Advanced</h3>
      <p class="copy">Die Haut wirkt insgesamt erfrischt, vitalisiert und gestrafft. Feine Linien und Fältchen werden reduziert.</p>
      <p class="duration">Dauer: 50-70 Minuten (je nach Peeling)</p>
      <span class="badge">€ 99</span>
    </div>
    <div class="item">
      <h3 class="item-title">Chemisches Peeling<br>(Oktober – April)</h3>
      <p class="copy">Professionelle Peelings können viele Problemstellungen lindern, verbessern oder gar beheben. Dazu gehören die Zellerneuerung, Glättung der Hautextur, Reduzierung von Pigmentflecken, Verbesserung von Akne.</p>
    </div>
  </article>

  <article class="panel panel--gold device">
    <h2 class="menu-heading">Apparative Behandlungen</h2>
    <h3 class="item-title">AquaVeil – „Glowing Skin“ Treatment</h3>
    <p class="copy" style="font-size:11px">In 6 Schritten zu einer Haut mit einmaligem Glow-Effekt</p>
    <ol class="steps">
      <li>Behandlungsschritt: die Haut wird tiefengereinigt</li>
      <li>Behandlungsschritt: die obersten Verhornungen und Schuppen werden sanft mit einem Peeling gelöst</li>
      <li>Behandlungsschritt: die Haut wird in der Tiefe gereinigt und entschlackt</li>
      <li>Behandlungsschritt: niedermolekulare Wirkstoffe werden aufgebracht, um die Haut zu erfrischen und den entsprechenden Glow zu geben</li>
      <li>Ausgewählte und hochdosierte Wirkstoffessenzen werden auf die Haut gesprüht und durch die niedrige Molekularstruktur können diese tiefer in der Haut wirken</li>
      <li>Zum Schluss werden die Essenzen durch eine impulsgebende Druckluftmassage noch tiefer in die Haut gebracht</li>
    </ol>
    <p class="duration">Dauer: 60 Minuten</p>
    <span class="badge badge--slate">€ 140</span>
  </article>

  <div class="footer-band">Lena Tessmar Hautatelier – Lindenstieg 17 · 83671 Ostermoor</div>
</section>

</body>
</html>
```